Web Design Project

We are an IT System Integrator. We provide Norvik 500 ERP System, CRM etc. We also provide hardware, networking servicing. Please look at www.brinquot.com.sg. They provide the same service as us. We like to redesign our web site. I will attached the color that I prefer for reference.

Our website is www.ravdu.com.sg.  It has been created about 14 years ago.  We are trying to revamp it with a new look and information.   The new website must be informative, fast.    I have attached an attachment which show the color that I prefer(brownish golden).   

Our competitor (www.brinquot.com) is carrying the same trade as us.  They have all the informations In their website that we will like to have.  Therefore I recommend you to take a look at my competitor website and have a better   
understanding on the kind of information I would like to have for my new website.

This project is guarantee to the person with the best design.  We can have it guarantee.

Target Market(s)

Corporate and companies

Industry/Entity Type

Hardware

```html
<!DOCTYPE html>
<html lang="en">
<head>
<meta charset="utf-8">
<title>Ravdu Information Systems Pte Ltd</title>
<link rel="stylesheet" href="https://fonts.googleapis.com/css2?family=Open+Sans:ital,wght@0,400;0,600;0,700;1,400&family=Oswald:wght@400;500&family=Lora:ital@1&display=swap">
<style>
:root{
  --orange:#e08a1c;
  --orange-light:#f3a93a;
  --orange-dark:#c5620f;
  --beige:#f4ebdc;
  --cream:#f7e8cf;
  --footer:#efece6;
  --text:#555;
  --muted:#9a9a9a;
  --dark:#333;
  --line:#dcdcdc;
  --ring:#79c6ea;
  --label:#3a9ed3;
  --badge:#c8281b;
  --white:#fff;
}
*{box-sizing:border-box;margin:0;padding:0}
html,body{width:1200px;height:2345px;overflow:hidden}
body{position:relative;background:var(--white);font-family:"Open Sans",Arial,sans-serif;color:var(--text)}
.abs{position:absolute}
.top-band{left:0;top:0;width:1200px;height:508px;background:var(--beige)}
.brand{left:133px;top:26px;display:flex;align-items:center;gap:10px}
.brand-mark{width:46px;height:46px;background:var(--orange)}
.brand-name{font-weight:700;font-size:17px;line-height:19px;color:var(--orange-dark);text-transform:uppercase;width:180px}
.utility{right:132px;top:4px;font-size:12px;color:var(--muted);display:flex;gap:8px}
.utility .sep{color:#ccc}
.login{left:561px;top:47px;display:flex;gap:12px}
.login .field{height:31px;background:#e6e0d6;border-radius:2px;font-size:13px;color:#666;padding:6px 8px}
.login .user{width:205px}.login .pass{width:209px}
.login .btn{width:71px;height:31px;border-radius:3px;background:linear-gradient(#f1a12c,#d97c0c);color:#4a2a00;font-size:14px;font-weight:600;text-align:center;line-height:31px;margin-left:-2px}
.nav{left:133px;top:98px;width:935px;height:43px;border-radius:4px;background:linear-gradient(#f6b342,#e08a1c 55%,#d3750c);display:flex;box-shadow:0 2px 3px rgba(0,0,0,.15)}
.nav a{flex:1;color:var(--white);font-size:13px;font-weight:600;text-align:center;line-height:43px;text-decoration:none;border-right:1px solid rgba(255,255,255,.35)}
.nav a:last-child{border-right:0}
.hero{left:133px;top:188px;width:935px;height:398px;background:var(--white);padding:8px;box-shadow:0 3px 8px rgba(0,0,0,.15)}
.hero-photo{position:absolute;left:8px;top:8px;width:919px;height:382px;background:linear-gradient(90deg,#8a8178,#5b5149 45%,#3f3731)}
.hero-title{left:575px;top:60px;font-family:"Oswald",sans-serif;color:var(--white);font-size:50px;line-height:48px;font-weight:500;letter-spacing:1px}
.hero-title small{font-size:26px}
.hero-copy{left:577px;top:172px;width:300px;color:var(--white);font-size:15px;line-height:23px;font-weight:600}
.dots{left:26px;top:357px;display:flex;gap:5px}
.dots i{width:10px;height:10px;border-radius:50%;background:#ddd;display:block}
.dots i:first-child{background:var(--white);border:2px solid #999}
.welcome-kicker{left:131px;top:626px;font-family:"Lora",serif;font-style:italic;font-size:20px;color:var(--dark)}
.welcome-title{left:131px;top:648px;font-size:22px;font-weight:600;color:var(--orange-dark)}
.welcome-lead{left:131px;top:686px;width:630px;font-size:17px;line-height:25px;font-weight:600;color:#9b9b9b}
.welcome-lead b{color:var(--orange-dark);font-weight:600}
.welcome-body{left:131px;top:772px;width:622px;font-size:14px;line-height:21.5px;color:var(--muted)}
.solutions-title{left:131px;top:962px;font-size:23px;color:var(--orange-dark);font-weight:600}
.solutions-title span{color:var(--dark);font-weight:400}
.solutions{left:131px;top:1012px;width:620px;display:grid;grid-template-columns:217px 200px 200px;row-gap:12px;font-size:14px;color:var(--muted)}
.solutions li{list-style:none;display:flex;align-items:center;gap:8px}
.diagram-ring{left:190px;top:1130px;width:430px;height:430px;border-radius:50%;border:1.5px solid var(--ring)}
.diagram-label{left:133px;top:1327px;width:112px;height:28px;background:var(--white);color:var(--label);font-size:21px;font-weight:700;text-align:center;line-height:28px;border-left:1.5px solid var(--ring);border-bottom:1.5px solid var(--ring)}
.product-box{background:linear-gradient(135deg,#e6f2f8,#9ccde5 60%,#4e9cc7);box-shadow:2px 3px 5px rgba(0,0,0,.2)}
.tab{background:linear-gradient(#f3a23a,#dc7c14);color:var(--white);font-size:14px;font-weight:600;border-radius:6px 6px 0 0;padding:3px 10px;white-space:nowrap}
.news{left:788px;top:635px;width:280px;height:551px;background:var(--white);border:1px solid var(--line);box-shadow:0 2px 5px rgba(0,0,0,.12)}
.news-head{height:58px;background:linear-gradient(#f4aa3d,#dc7c14);color:var(--white);font-size:23px;font-weight:600;padding:12px 16px;border-radius:3px 3px 0 0}
.news-item{position:absolute;left:18px;width:245px}
.news-date{display:inline-flex;align-items:center;gap:6px;background:#efe3cf;font-size:11.5px;color:var(--dark);padding:2px 8px}
.news-date i{width:9px;height:9px;background:#555;display:block}
.news-title{font-size:12.5px;line-height:17px;color:var(--orange-dark);margin-top:8px}
.news-text{font-size:12.5px;line-height:17px;color:var(--dark);margin-top:7px}
.testi-title{left:788px;top:1218px;font-size:23px;font-weight:600;color:var(--orange-dark)}
.testi-box{left:788px;top:1260px;width:280px;height:240px;background:var(--cream);padding:16px 20px;font-size:12.5px;line-height:19.5px;color:var(--dark)}
.testi-box:after{content:"";position:absolute;left:30px;bottom:-14px;border:8px solid transparent;border-top:8px solid var(--cream);border-left:8px solid var(--cream)}
.testi-badge{left:788px;top:1531px;width:52px;height:58px;background:var(--badge)}
.testi-author{left:853px;top:1528px;font-size:13px;line-height:17px;color:var(--badge)}
.testi-author span{color:var(--dark)}
.partners-title{left:0;top:1658px;width:1200px;text-align:center;font-size:28px;font-weight:500;color:var(--orange-dark);letter-spacing:1px}
.partners-rule{top:1680px;height:1px;width:290px;background:#e3d8c5}
.partner{width:146px;height:146px;border-radius:50%;border:1px solid #ddd;background:var(--white);top:1734px}
.partner i{position:absolute;left:33px;top:50px;width:80px;height:44px;border-radius:6px;background:#cfcfcf;display:block}
.footer{left:0;top:1934px;width:1200px;height:362px;background:var(--footer)}
.fcol{top:1960px;font-size:13px;line-height:22.2px;color:var(--text)}
.fcol h4{font-size:14.5px;font-weight:700;color:var(--dark);margin-bottom:4px;line-height:20px}
.fcol ul{list-style:none}
.contact{left:845px;top:1958px;width:223px;height:314px;background:var(--white);border-radius:5px;padding:12px 18px;font-size:14px;line-height:21px;color:var(--text)}
.contact h4{font-size:14.5px;font-weight:700;color:var(--dark);margin-bottom:12px}
.contact .social{display:flex;gap:10px;margin-top:28px}
.contact .social i{width:42px;height:42px;border-radius:50%;border:1px solid #ddd;display:block;background:#f6efe4}
.bottom{left:0;top:2296px;width:1200px;height:49px;background:linear-gradient(#d07a22,#b85f14);color:#fbe3c6;font-size:12.5px}
.bottom .copy{position:absolute;left:131px;top:15px}
.bottom .links{position:absolute;right:132px;top:15px;display:flex;gap:18px;color:var(--white)}
</style>
</head>
<body>
<div class="abs top-band"></div>

<header>
  <div class="abs brand"><span class="brand-mark"></span><span class="brand-name">Ravdu Information Systems Pte Ltd</span></div>
  <div class="abs utility"><span>Sitemap</span><span class="sep">|</span><span>Logincident</span><span class="sep">|</span><span>Enquiry</span><span class="sep">|</span><span>Client Support</span><span class="sep">|</span><span>Contact</span></div>
  <div class="abs login"><div class="field user">User Name :</div><div class="field pass">Password :</div><div class="btn">LOGIN</div></div>
  <nav class="abs nav"><a>HOME</a><a>COMPANY</a><a>PRODUCTS</a><a>NORVIK</a><a>SERVICES</a><a>CLIENTELE</a><a>CAREERS</a><a>INFOBIN</a><a>CONTACT</a></nav>
</header>

<section class="abs hero">
  <div class="hero-photo" role="img" aria-label="Warehouse aisle with a businessman holding a clipboard"></div>
  <h1 class="abs hero-title">WHOLESALE <small>&amp;</small><br>DISTRIBUTIONS</h1>
  <p class="abs hero-copy">Increase profitability with clear visibility of inventory levels and the status of customer and supplier accounts.</p>
  <div class="abs dots"><i></i><i></i><i></i><i></i><i></i></div>
</section>

<section>
  <p class="abs welcome-kicker">Welcome to</p>
  <h2 class="abs welcome-title">Ravdu Information Systems Pte Ltd</h2>
  <p class="abs welcome-lead">Based in Singapore with <b>11 years</b> of establishment, <b>250 local &amp; regional</b> customers, <b>300 project</b> implementations, <b>1000 satisfied users</b> and we are still growing.</p>
  <p class="abs welcome-body">Ravdu Information Systems Pte Ltd (RIS) is professionally managed by a core group of visionaries and technologists with decades of industry experience between them and backed by a team of trained professionals at all levels of operations. Perfection is a way of life at RIS. The organization has grown from a small beginning in 1993, to become a company of international repute for reliability. RIS has transformed from an NORVIK Reseller to a company providing total IT solutions to companies in Singapore and the Asia region. RIS provides hardware maintenance, networking, software and consulting services.</p>
  <h3 class="abs solutions-title">IT Solutions - <span>Beginning in 1993</span></h3>
  <ul class="abs solutions">
    <li><svg width="14" height="14" viewBox="0 0 14 14"><circle cx="7" cy="7" r="6" fill="none" stroke="#aaa"/><path d="M4 7.2l2 2 4-4.4" fill="none" stroke="#999" stroke-width="1.5"/></svg>Hardware</li>
    <li><svg width="14" height="14" viewBox="0 0 14 14"><circle cx="7" cy="7" r="6" fill="none" stroke="#aaa"/><path d="M4 7.2l2 2 4-4.4" fill="none" stroke="#999" stroke-width="1.5"/></svg>Networking</li>
    <li><svg width="14" height="14" viewBox="0 0 14 14"><circle cx="7" cy="7" r="6" fill="none" stroke="#aaa"/><path d="M4 7.2l2 2 4-4.4" fill="none" stroke="#999" stroke-width="1.5"/></svg>Consulting Services</li>
    <li><svg width="14" height="14" viewBox="0 0 14 14"><circle cx="7" cy="7" r="6" fill="none" stroke="#aaa"/><path d="M4 7.2l2 2 4-4.4" fill="none" stroke="#999" stroke-width="1.5"/></svg>Maintenance</li>
    <li><svg width="14" height="14" viewBox="0 0 14 14"><circle cx="7" cy="7" r="6" fill="none" stroke="#aaa"/><path d="M4 7.2l2 2 4-4.4" fill="none" stroke="#999" stroke-width="1.5"/></svg>Software</li>
  </ul>
</section>

<section class="product-diagram">
  <div class="abs diagram-ring"></div>
  <div class="abs diagram-label">NORVIK</div>
  <div class="abs product-box" style="left:268px;top:1280px;width:113px;height:127px" role="img" aria-label="Summit Series software box"></div>
  <div class="abs product-box" style="left:381px;top:1309px;width:95px;height:108px" role="img" aria-label="Warehouse Management System software box"></div>
  <div class="abs product-box" style="left:453px;top:1270px;width:110px;height:100px" role="img" aria-label="CRM software box"></div>
  <div class="abs product-box" style="left:547px;top:1309px;width:98px;height:98px" role="img" aria-label="eTradeway software box"></div>
  <div class="abs product-box" style="left:660px;top:1266px;width:95px;height:128px" role="img" aria-label="ePOS software box"></div>
  <div class="abs tab" style="left:268px;top:1254px">Summit Series</div>
  <div class="abs tab" style="left:488px;top:1244px">CRM</div>
  <div class="abs tab" style="left:553px;top:1288px">eTradeway</div>
  <div class="abs tab" style="left:676px;top:1243px">ePOS</div>
  <div class="abs tab" style="left:383px;top:1411px;border-radius:0 0 6px 6px">Warehouse Management System</div>
</section>

<aside class="abs news">
  <div class="news-head">Recent News</div>
  <div class="news-item" style="top:72px"><span class="news-date"><i></i>25 March, 2013</span><p class="news-title">Expanding the Boundaries with QuillDM-ERP Integration Workshop</p><p class="news-text">You are invited to attend the Expanding the Boundaries with QuillDM-ERP Integration workshop. There are many functions &amp; values offers</p></div>
  <div class="news-item" style="top:230px"><span class="news-date"><i></i>25 March, 2013</span><p class="news-title">Expanding the Boundaries with QuillDM-ERP Integration Workshop</p><p class="news-text">You are invited to attend the Expanding the Boundaries with QuillDM-ERP Integration workshop. There are many functions &amp; values offers</p></div>
  <div class="news-item" style="top:388px"><span class="news-date"><i></i>25 March, 2013</span><p class="news-title">Expanding the Boundaries with QuillDM-ERP Integration Workshop</p><p class="news-text">You are invited to attend the Expanding the Boundaries with QuillDM-ERP Integration workshop. There are many functions &amp; values offers</p></div>
</aside>

<section>
  <h3 class="abs testi-title">Testimonials</h3>
  <blockquote class="abs testi-box">"The professionalism of Ravdu Information Systems and the long-time relationship between KLF and Ravdu are major considerations for NWCU, NWCU Link and KLF in choosing the NORVIK Accounting Software. Ravdu's customer-focused approach, well-trained staff, and ability to provide customised solutions to its clients speak volumes of its competency as NORVIK's..."</blockquote>
  <div class="abs testi-badge"></div>
  <p class="abs testi-author">Project Manager,<br>Information Technology at NWCU<br><span>(National Workers Commerce Union)</span></p>
</section>

<section>
  <div class="abs partners-rule" style="left:230px"></div>
  <h3 class="abs partners-title">PARTNERS</h3>
  <div class="abs partners-rule" style="left:680px"></div>
  <div class="abs partner" style="left:176px"><i></i></div>
  <div class="abs partner" style="left:342px"><i></i></div>
  <div class="abs partner" style="left:518px"><i></i></div>
  <div class="abs partner" style="left:707px"><i></i></div>
  <div class="abs partner" style="left:889px"><i></i></div>
</section>

<footer>
  <div class="abs footer"></div>
  <div class="abs fcol" style="left:131px"><h4>ABOUT US</h4><ul><li>Profile</li><li>Partners</li><li>Management Team</li><li>Quality</li><li>Careers</li><li>Location</li></ul>
    <h4 style="margin-top:14px">CAREERS</h4><ul><li>Overview</li><li>Work Culture</li><li>Current Openings</li></ul></div>
  <div class="abs fcol" style="left:276px"><h4>PRODUCTS</h4><ul><li>Overview</li><li>Workstations</li><li>Servers</li><li>Printers</li><li>Surveillance Camera</li></ul>
    <h4 style="margin-top:8px">INFOBIN</h4><ul><li>New Releases</li><li>News Room</li><li>Downloads</li><li>Events</li><li>Awards</li></ul></div>
  <div class="abs fcol" style="left:420px"><h4>NORVIK</h4><ul><li>Business Solutions</li><li>Summit Series</li><li>eTradeway</li><li>CRM</li><li>CFO</li><li>WMS</li><li>ePOS</li><li>Perspective</li></ul></div>
  <div class="abs fcol" style="left:556px"><h4>SERVICES</h4><ul><li>Overview</li><li>Technical Services</li><li>Custom Prog.Solutions</li><li>Tailored Reporting</li><li>Maintenance Contracts</li><li>Training</li><li>Email Solutions</li><li>Internet Security</li><li>Hardware &amp; Peripherals</li><li>Management Services</li></ul></div>
  <div class="abs fcol" style="left:730px"><h4>CLIENTELE</h4><ul><li>Overview</li><li>Client List</li><li>Testimonials</li><li>Awards</li><li>Success Stories</li></ul></div>
  <div class="abs contact">
    <h4>CONTACT</h4>
    <p>Ravdu Information<br>Systems Pte Ltd<br>18 Keltan Road<br>#05-21/22 Orchid Point<br>Singapore - 579812</p>
    <p style="margin-top:14px"><b>T:</b> (065) 6100-2480<br><b>E:</b> info@ravdu-user.com</p>
    <div class="social"><i></i><i></i></div>
  </div>
  <div class="abs bottom"><span class="copy">© 2013 Ravdu Information Systems. All rights reserved.</span><span class="links"><span>Home</span><span>Terms &amp; Conditions</span><span>Privacy Policy</span><span>Sitemap</span></span></div>
</footer>
</body>
</html>
```